Package Design - Disposable Face Towel

Hi,

We are needing assistance with graphic design on our box/carton/package.

The attached image that is white is our biggest competitor.

Our brand is "BRIGHT DEW LABS" Please see the logo we uploaded.

Oder we have in mind for front of box:

Logo
LARGE TOWELS
50 Count
Ultra Soft| 100% CERTIFIED Bio-Based|100% Eucalyptus Viscose | Vegan
BRIGHTDEWLABS.EXAMPLE

We like medium to dark blue on most of the box, with white and minimal hot pink or salmon. Something that is sharp, modern, and stands out from our competitors.

Box dimensions are: 6.25 x 5.25 x 4.75 inches

This will be 1 of many design projects.

Target Market(s)

Female Beauty Products

Font styles to use
Serif
Sans Serif

Colors
0054AA
0677BA
7BADD7
CADEEF
E8F1F8
EB3D1F
EC4F4E
F09395
F8D3D4
FCEDEE

Requirements
Must have
• Needs to look sharp and modern

```html
<!DOCTYPE html>
<html lang="en">
<head>
<meta charset="utf-8">
<title>Bright Dew Labs – XL Dew Cloths Carton Dieline</title>
<link rel="stylesheet" href="https://fonts.googleapis.com/css2?family=Raleway:wght@300;400;600&display=swap">
<style>
  :root {
    --paper: #ffffff;
    --carton-blue: #547bbb;
    --band-cyan: #74c8db;
    --band-pink: #e0177e;
    --band-light: #dfe8f3;
    --ink-white: #ffffff;
    --cut-line: #1d1d1d;
    --perforation: #3a4f78;
  }
  * { box-sizing: border-box; margin: 0; padding: 0; }
  html, body { width: 1200px; height: 749px; overflow: hidden; background: var(--paper); }
  body { position: relative; font-family: "Raleway", sans-serif; color: var(--ink-white); }

  .panel {
    position: absolute;
    background: var(--carton-blue);
    border: 0.6px solid var(--cut-line);
    overflow: hidden;
  }
  .flap-top    { left: 167px; top: 140px; width: 183px; height: 139px; }
  .side-left   { left: 167px; top: 279px; width: 183px; height: 153px; border-left: none; }
  .side-info   { left: 350px; top: 279px; width: 183px; height: 153px; }
  .front       { left: 533px; top: 279px; width: 183px; height: 153px; }
  .side-right  { left: 716px; top: 279px; width: 184px; height: 153px; }
  .flap-bottom { left: 350px; top: 432px; width: 183px; height: 139px; }

  .wordmark {
    position: absolute;
    left: 0; right: 0;
    text-align: center;
    font-weight: 300;
    letter-spacing: 0.03em;
    line-height: 1.05;
    color: var(--ink-white);
  }
  .wordmark.large { top: 34px; font-size: 15px; }
  .wordmark.small { top: 11px; font-size: 9px; }
  .flap-top .wordmark { top: 30px; font-size: 13px; }
  .flap-bottom .wordmark { top: 56px; font-size: 15px; }

  .band-stack { position: absolute; left: 0; right: 0; }
  .band-light { height: 2px; background: var(--band-light); }
  .band-cyan {
    height: 14px; background: var(--band-cyan);
    font-size: 8.5px; font-weight: 400; text-align: center; line-height: 14px;
    color: var(--ink-white); letter-spacing: 0.02em;
  }
  .band-gap { height: 1.5px; background: var(--band-light); }
  .band-pink { height: 2px; background: var(--band-pink); }
  .panel .band-stack { top: 97px; }
  .flap-top .band-stack { top: 101px; }
  .flap-top .band-cyan { height: 12px; line-height: 12px; font-size: 7.5px; }

  .count { position: absolute; top: 127px; left: 0; right: 0; text-align: center; font-size: 4.4px; font-weight: 600; }
  .claims { position: absolute; top: 135px; left: 0; right: 0; text-align: center; font-size: 4.2px; letter-spacing: 0.01em; white-space: nowrap; }
  .side-info .claims { top: 132px; left: 11px; right: auto; text-align: left; font-size: 3.6px; }
  .web-address {
    position: absolute; top: 142px; left: 50%; transform: translateX(-50%);
    background: var(--ink-white); color: var(--carton-blue);
    font-size: 4.2px; padding: 1px 2px 4px; white-space: nowrap;
  }

  .badge { position: absolute; border: 0.8px solid var(--ink-white); border-radius: 2px; }
  .badge.mini { top: 6px; right: 8px; width: 10px; height: 12px; }
  .badge.wide { top: 123px; right: 9px; width: 19px; height: 22px; border-radius: 3px; }

  .purpose { position: absolute; left: 20px; right: 20px; top: 44px; font-size: 4.1px; line-height: 1.3; }
  .purpose h2 { font-size: 4.4px; font-weight: 400; }

  .perforation {
    position: absolute; left: 193px; top: 208px; width: 130px; height: 152px;
    border: 0.6px dashed var(--perforation); border-radius: 5px; pointer-events: none;
  }
</style>
</head>
<body>

  <section class="panel flap-top">
    <div class="wordmark">BRIGHT DEW<br>LABS</div>
    <div class="band-stack">
      <div class="band-light"></div>
      <div class="band-cyan">XL DEW CLOTHS</div>
      <div class="band-gap"></div>
      <div class="band-pink"></div>
    </div>
  </section>

  <section class="panel side-left">
    <div class="badge mini" role="img" aria-label="Certification badge"></div>
    <div class="wordmark large">BRIGHT DEW<br>LABS</div>
    <div class="band-stack">
      <div class="band-light"></div>
      <div class="band-cyan">XL DEW CLOTHS</div>
      <div class="band-gap"></div>
      <div class="band-pink"></div>
    </div>
    <p class="count">50 COUNT</p>
    <p class="claims">ULTRA SOFT I 100% CERTIFIED BIO - BASED I 100%EUCALYPTUS VISCOSE I VEGAN</p>
    <p class="web-address">BRIGHTDEWLABS.EXAMPLE</p>
  </section>

  <section class="panel side-info">
    <div class="wordmark small">BRIGHT DEW<br>LABS</div>
    <div class="purpose">
      <h2>TOWEL PORPOSE</h2>
      <p>Lorem josum dole si amet consent alpiscingeli, sed do eismod tempor incatium ut labore et dolore magna liqua. Utenim a minin veniam quis moshod eectation ulano letoris nix alpiperea commodo consequat. Duis aute inure dolorin repreheneni in voluptate veli esse allum dolore eu hugiat null pariatu. Erceptew sint oceaecatapiaiat on poident suntin aipe qui officiadeserunt molt anin it es abou</p>
    </div>
    <div class="band-stack">
      <div class="band-light"></div>
      <div class="band-cyan"></div>
      <div class="band-gap"></div>
      <div class="band-pink"></div>
    </div>
    <p class="claims">ULTRA SOFT I 100% CERTIFIED BIO - BASED I 100%EUCALYPTUS VISCOSE I VEGAN</p>
    <div class="badge wide" role="img" aria-label="Organic certification badge"></div>
  </section>

  <section class="panel front">
    <div class="badge mini" role="img" aria-label="Certification badge"></div>
    <div class="wordmark large">BRIGHT DEW<br>LABS</div>
    <div class="band-stack">
      <div class="band-light"></div>
      <div class="band-cyan">XL DEW CLOTHS</div>
      <div class="band-gap"></div>
      <div class="band-pink"></div>
    </div>
    <p class="count">50 COUNT</p>
    <p class="claims">ULTRA SOFT I 100% CERTIFIED BIO - BASED I 100%EUCALYPTUS VISCOSE I VEGAN</p>
    <p class="web-address">BRIGHTDEWLABS.EXAMPLE</p>
  </section>

  <section class="panel side-right">
    <div class="badge mini" role="img" aria-label="Certification badge"></div>
    <div class="wordmark large">BRIGHT DEW<br>LABS</div>
    <div class="band-stack">
      <div class="band-light"></div>
      <div class="band-cyan">XL DEW CLOTHS</div>
      <div class="band-gap"></div>
      <div class="band-pink"></div>
    </div>
    <p class="count">50 COUNT</p>
    <p class="claims">ULTRA SOFT I 100% CERTIFIED BIO - BASED I 100%EUCALYPTUS VISCOSE I VEGAN</p>
    <p class="web-address">BRIGHTDEWLABS.EXAMPLE</p>
  </section>

  <section class="panel flap-bottom">
    <div class="wordmark">BRIGHT DEW<br>LABS</div>
  </section>

  <div class="perforation" aria-hidden="true"></div>

</body>
</html>
```